Buch-/eBook-Cover für Anti-Stress-Adventskalender
Zielgruppe
Wir sind als Selfpublisher vorwiegend bei Lorvan PDX aktiv und veröffentlichen Taschenbücher im Bereich Sachbücher, Ratgeber und Kinderbücher. Die Zielgruppe ist bei diesem Projekt schwieriger zu bestimmten, aber wird vsl. im Bereich der jungen Erwachsenen liegen und tendenziell eher im weiblichen Publikum.
Aufgabenstellung
Das Design sollte ein individuell auf das Projekt und auf die Zielgruppe abgestimmtes Konzept verfolgen, welches auf Lorvan in die Augen sticht und Besteller Potential hat. Es sollte sich an bereits vorhanden Bestsellern in der jeweiligen Nische orientieren und dabei trotzdem die eigene Idee verdeutlichen. Der Sarkasmus und Humor des Buches und des Haupttitels sollte aus dem Cover hervorgehen.
Der Haupttitel: 17 Tricks, dem Christkind nicht die Geduld zu rauben
Der Nebentitel: Dein lustiger Anti-Stress Adventskalender mit außergewöhnlichen Witzen, Rätseln und kreativen Aufgaben.
Autor: Jonas Falkner
Die Maße des Taschenbuchs werden wie folgt sein: 15.24 x 0.64 x 22.86 cm

```html
<!DOCTYPE html>
<html lang="de">
<head>
<meta charset="utf-8">
<title>17 Tricks, dem Christkind nicht die Geduld zu rauben – Cover</title>
<link rel="stylesheet" href="https://fonts.googleapis.com/css2?family=Permanent+Marker&family=Rubik+Dirt&family=Caveat+Brush&family=Gochi+Hand&family=Patrick+Hand&display=swap">
<style>
  :root {
    --page-bg: #f1efec;
    --night: #1f2350;
    --night-mid: #3d4a76;
    --mist: #a9c4c9;
    --mist-light: #d9e7e8;
    --snow: #ffffff;
    --ink: #111111;
    --green: #4f8a2c;
    --author: #3a4a6a;
    --character-red: #b0293a;
    --character-hair: #dfe4ea;
  }
  * { margin: 0; padding: 0; box-sizing: border-box; }
  html, body {
    width: 1200px; height: 846px; overflow: hidden;
    background: var(--page-bg);
  }
  .canvas {
    position: relative; width: 1200px; height: 846px;
    display: flex; align-items: center; justify-content: center;
  }
  .cover {
    position: relative; width: 520px; height: 780px; overflow: hidden;
    background: linear-gradient(180deg, var(--night) 0%, var(--night-mid) 16%, var(--mist) 38%, var(--mist-light) 58%, var(--mist) 100%);
  }
  .swoosh { position: absolute; left: 0; top: 170px; width: 520px; height: 90px; }
  .note {
    position: absolute; left: 60px; top: 52px; width: 146px; height: 140px;
    background: var(--snow); transform: rotate(-4deg);
    box-shadow: 0 3px 8px rgba(0,0,0,.25);
  }
  .note::before, .note::after {
    content: ""; position: absolute; top: -10px; width: 40px; height: 18px;
    background: rgba(230,230,230,.85);
  }
  .note::before { left: -8px; transform: rotate(-30deg); }
  .note::after { right: -8px; transform: rotate(30deg); }
  .note-number {
    position: absolute; left: 70px; top: 68px; width: 130px; text-align: center;
    font-family: "Permanent Marker", cursive; font-size: 84px; line-height: 1;
    color: var(--green); transform: rotate(-4deg);
  }
  .title-main {
    position: absolute; left: 208px; top: 92px;
    font-family: "Permanent Marker", cursive; font-size: 90px; line-height: 1;
    color: var(--ink); -webkit-text-stroke: 2px var(--snow); paint-order: stroke fill;
    text-shadow: 0 0 6px rgba(255,255,255,.8);
  }
  .title-line {
    position: absolute; left: 0; width: 520px; text-align: center;
    font-family: "Rubik Dirt", sans-serif; color: var(--ink);
    text-shadow: 0 0 5px #fff, 0 0 3px #fff;
  }
  .title-line.first { top: 214px; font-size: 40px; }
  .title-line.second { top: 262px; font-size: 30px; }
  .title-line .accent {
    font-family: "Caveat Brush", cursive; color: var(--green);
    font-size: 46px; margin-right: 6px; vertical-align: -4px;
  }
  .subtitle {
    position: absolute; left: 30px; top: 344px; width: 440px;
    padding: 8px 12px; background: rgba(255,255,255,.92);
    border-radius: 6px;
    font-family: "Gochi Hand", cursive; font-size: 22px; line-height: 1.17;
    color: var(--ink);
  }
  .illustration {
    position: absolute; left: 40px; top: 440px; width: 440px; height: 340px;
    background: radial-gradient(ellipse at 30% 60%, var(--character-hair) 0%, #c9a2ad 35%, transparent 60%),
                radial-gradient(ellipse at 72% 55%, var(--character-red) 0%, #c45563 30%, transparent 58%);
    border-radius: 40px 40px 0 0;
  }
  .snowbank { position: absolute; left: 0; bottom: 0; width: 520px; height: 90px; }
  .author {
    position: absolute; right: 58px; bottom: 34px;
    font-family: "Patrick Hand", cursive; font-size: 24px; letter-spacing: 1px;
    color: var(--author);
  }
</style>
</head>
<body>
<div class="canvas">
  <section class="cover">
    <svg class="swoosh" viewBox="0 0 520 90" aria-hidden="true">
      <path d="M40 70 Q 260 10 520 40 L520 48 Q 270 22 40 74 Z" fill="#ffffff" opacity="0.85"/>
    </svg>

    <div class="note" aria-hidden="true"></div>
    <div class="note-number">17</div>
    <h1>
      <span class="title-main">Tricks,</span>
      <span class="title-line first">dem Christkind</span>
      <span class="title-line second"><span class="accent">nicht</span>die Geduld zu rauben</span>
    </h1>

    <p class="subtitle">Dein lustiger Anti-Stress Adventskalender mit außergewöhnlichen Witzen, Rätseln und kreativen Aufgaben.</p>

    <div class="illustration" role="img" aria-label="Illustration: genervte junge Frau mit Weihnachtsmütze und geballten Fäusten, daneben ein erschrockener Weihnachtsmann"></div>

    <svg class="snowbank" viewBox="0 0 520 90" aria-hidden="true">
      <path d="M0 70 Q 120 60 260 50 Q 380 20 520 10 L520 90 L0 90 Z" fill="#ffffff"/>
    </svg>
    <p class="author">JONAS FALKNER</p>
  </section>
</div>
</body>
</html>
```